Memento Mori Calendar

I’m looking for a graphic designer to create a Memento Mori–style life calendar that captures the essence of QUILNEXA — minimal, timeless, and deeply philosophical.

The design should be black and white only, with a refined, clean aesthetic and a sense of stillness and precision.
It should feel modern yet eternal, reflecting the themes of time, mortality, and presence.

Deliverables (Print-Ready Files):

24 x 30 in

24 x 32 in

24 x 36 in

A1 (594 x 841 mm)

All formats should be high-resolution and ready for professional printing (300 DPI, CMYK).

Design Requirements:

The calendar layout should follow the Memento Mori life calendar concept (weeks of life represented as small squares or circles).

The overall tone: minimal, meditative, monochrome.

Include the brand name: QUILNEXA (in an elegant, understated placement).

Add the following quote at the bottom or in a subtle position:

“Life can only be understood backwards; but it must be lived forwards.”
— Anselm Brodtvik

Target Market(s)

The QUILNEXA audience consists of urban, creative individuals aged 25 to 45, belonging to a middle to upper-middle income class. They lead conscious, quietly ambitious lives, seeking balance between inner depth and modern design. Their values center on awareness, presence, authenticity, and emotional depth, reflected in their preference for a monochrome, minimal, and timeless aesthetic. They tend to be introverted, reflective, and spiritually curious, drawn to brands that embody meaning and restraint rather than excess. Their cultural and stylistic affinities include Vinth, Polde, Ro Sefi, The Garden of Hours, Dussant, and Varolé — labels that share QUILNEXAs devotion to simplicity, substance, and subtle ritual.

Font styles to use
Serif
Sans Serif

Colors

Designer to choose only greyscale colors for use in the design.

Requirements
Must have
• The calendar layout should follow the Memento Mori life calendar concept (weeks of life represented as small squares or circles). The overall tone: minimal, meditative, monochrome. Include the brand name: trvolquen (in an elegant, understated placement). Add the following quote at the bottom or in a subtle position: “Life can only be understood backwards; but it must be lived forwards.” — Anselm Brodtvik

```html
<!DOCTYPE html>
<html lang="en">
<head>
<meta charset="utf-8">
<title>Memento Mori Life Calendar — QUILNEXA</title>
<link href="https://fonts.googleapis.com/css2?family=Montserrat:wght@200;400&display=swap" rel="stylesheet">
<style>
  :root {
    --backdrop: #ffffff;
    --paper: #f5f5f5;
    --spine: #ebebeb;
    --ink: #111111;
    --cell: #9a9a9a;
    --axis: #b5b5b5;
    --label: #8a8a8a;
  }
  html, body {
    margin: 0;
    width: 1200px;
    height: 1200px;
    overflow: hidden;
    background: var(--backdrop);
  }
  .poster {
    position: absolute;
    left: 217px;
    top: 49px;
    width: 787px;
    height: 1114px;
    background: var(--paper);
    font-family: "Montserrat", sans-serif;
    color: var(--ink);
  }
  .spine {
    position: absolute;
    left: 34px;
    top: 0;
    width: 35px;
    height: 100%;
    background: var(--spine);
  }
  .brand {
    position: absolute;
    left: 51px;
    top: 1054px;
    transform: translate(-50%, -50%) rotate(-90deg);
    font-size: 11px;
    letter-spacing: 3.5px;
    font-weight: 400;
    white-space: nowrap;
  }
  .quote {
    position: absolute;
    right: 73px;
    top: 64px;
    margin: 0;
    text-align: right;
    font-size: 9.2px;
    line-height: 12.5px;
    font-weight: 400;
  }
  .quote cite { font-style: normal; display: block; }
  .title {
    position: absolute;
    left: 129px;
    top: 0;
    width: 0;
    margin: 0;
    font-weight: 200;
    font-size: 53px;
  }
  .title span {
    position: absolute;
    transform: translateX(-50%);
    line-height: 1;
  }
  .weeks {
    position: absolute;
    left: 0;
    top: 0;
  }
  .weeks .age { font-family: "Montserrat", sans-serif; font-size: 4.6px; fill: var(--label); }
</style>
</head>
<body>
<main class="poster">
  <div class="spine"></div>
  <div class="brand">QUILNEXA</div>

  <blockquote class="quote">
    “Life can only be understood backwards; but it must be lived forwards.”
    <cite>— Anselm Brodtvik</cite>
  </blockquote>

  <h1 class="title" aria-label="Memento Mori">
    <span style="top:162px">M</span>
    <span style="top:242px">E</span>
    <span style="top:323px">M</span>
    <span style="top:403px">E</span>
    <span style="top:484px">N</span>
    <span style="top:564px">T</span>
    <span style="top:645px">O</span>
    <span style="top:765px">M</span>
    <span style="top:846px">O</span>
    <span style="top:927px">R</span>
    <span style="top:1007px">I</span>
  </h1>

  <svg class="weeks" width="787" height="1114" viewBox="0 0 787 1114" aria-label="Weeks of an 80-year life">
    <defs>
      <pattern id="week" width="8.875" height="8.8" patternUnits="userSpaceOnUse">
        <rect x="0.3" y="0.3" width="6.8" height="6.8" fill="none" stroke="var(--cell)" stroke-width="0.5"/>
      </pattern>
      <g id="decade">
        <rect x="209" y="0" width="230.75" height="88" fill="url(#week)"/>
        <rect x="482" y="0" width="230.75" height="88" fill="url(#week)"/>
      </g>
    </defs>
    <use href="#decade" y="173"/>
    <use href="#decade" y="286.5"/>
    <use href="#decade" y="400"/>
    <use href="#decade" y="513.5"/>
    <use href="#decade" y="627"/>
    <use href="#decade" y="740.5"/>
    <use href="#decade" y="854"/>
    <use href="#decade" y="967.5"/>

    <line x1="720" y1="173" x2="720" y2="1055" stroke="var(--axis)" stroke-width="0.6"/>
    <g class="age">
      <text x="724" y="216">5</text><text x="724" y="260">10</text>
      <text x="724" y="329.5">15</text><text x="724" y="373.5">20</text>
      <text x="724" y="443">25</text><text x="724" y="487">30</text>
      <text x="724" y="556.5">35</text><text x="724" y="600.5">40</text>
      <text x="724" y="670">45</text><text x="724" y="714">50</text>
      <text x="724" y="783.5">55</text><text x="724" y="827.5">60</text>
      <text x="724" y="897">65</text><text x="724" y="941">70</text>
      <text x="724" y="1010.5">75</text><text x="724" y="1054.5">80</text>
    </g>
  </svg>
</main>
</body>
</html>
```